Click Buttons for our website

We need a Click button design for our website www.brevilo.dk:
- it should fit into our website's style and colors
- the buttons should be available in variable sizes (so they can accommodate from 1-7 word text)
- the buttons should be supplied as vector graphics (so we can resize them yourself)

The buttons are to replace the red text links we have on the site today, i.e. they are to be used to link to "contact us" page pdf's and such.

Brevilo is a Danish based IT Hosting and IT outsourcing Company selling business2business. our clients are medium sized companies with the need for It outsourcing.

```html
<!DOCTYPE html>
<html lang="en">
<head>
<meta charset="utf-8">
<title>Click buttons – Brevilo</title>
<link rel="stylesheet" href="https://fonts.googleapis.com/css2?family=Alfa+Slab+One&family=Archivo+Black&family=Open+Sans:wght@400&display=swap">
<style>
  :root {
    --bg: #4b4b4b;
    --bg-dark: #434343;
    --title-red: #d9163c;
    --subtitle: #b9b9b9;
    --btn-top: #4a4a4a;
    --btn-mid: #1e1e1e;
    --btn-bottom: #0b0b0b;
    --btn-edge: #000;
    --btn-text: #ffffff;
    --mark-red: #c8102e;
    --mark-ring: #5a0a14;
  }
  * { box-sizing: border-box; margin: 0; padding: 0; }
  html, body {
    width: 1200px;
    height: 900px;
    overflow: hidden;
  }
  body {
    position: relative;
    background: radial-gradient(ellipse at 40% 35%, var(--bg) 0%, var(--bg-dark) 100%);
  }
  .sheet-title {
    position: absolute;
    left: 160px;
    top: 56px;
    font-family: "Alfa Slab One", serif;
    font-size: 98px;
    line-height: 1;
    color: var(--title-red);
    letter-spacing: -1px;
    text-shadow: 0 4px 6px rgba(0, 0, 0, 0.55);
  }
  .sheet-subtitle {
    position: absolute;
    left: 176px;
    top: 184px;
    font-family: "Open Sans", sans-serif;
    font-size: 18px;
    letter-spacing: 4px;
    color: var(--subtitle);
    text-transform: uppercase;
  }
  .button-list {
    position: absolute;
    left: 176px;
    top: 282px;
    list-style: none;
  }
  .button-list li { height: 100px; }
  .button-list li + li { margin-top: 40px; }
  .click-button {
    display: flex;
    align-items: center;
    height: 100px;
    padding: 0 36px 0 32px;
    border-radius: 18px;
    border: 2px solid var(--btn-edge);
    background: linear-gradient(180deg, var(--btn-top) 0%, var(--btn-mid) 45%, var(--btn-bottom) 100%);
    box-shadow:
      inset 0 2px 1px rgba(255, 255, 255, 0.25),
      inset 0 -3px 4px rgba(0, 0, 0, 0.6),
      0 4px 8px rgba(0, 0, 0, 0.45);
    text-decoration: none;
    color: var(--btn-text);
    font-family: "Archivo Black", sans-serif;
    font-size: 28px;
    letter-spacing: 3px;
    text-transform: uppercase;
  }
  .click-button__mark {
    width: 56px;
    height: 56px;
    margin-right: 24px;
    flex: none;
  }
  .click-button--outsourcing { width: 458px; }
  .click-button--hosting { width: 354px; }
  .click-button--consulting { width: 602px; }
  .click-button--competences { width: 478px; }
</style>
</head>
<body>
  <h1 class="sheet-title">Click buttons</h1>
  <p class="sheet-subtitle">for www.brevilo.dk</p>

  <ul class="button-list">
    <li>
      <a class="click-button click-button--outsourcing" href="#">
        <svg class="click-button__mark" viewBox="0 0 56 56" aria-hidden="true"><circle cx="28" cy="28" r="25" fill="var(--mark-red)" stroke="var(--mark-ring)" stroke-width="3"/></svg>
        Outsourcing
      </a>
    </li>
    <li>
      <a class="click-button click-button--hosting" href="#">
        <svg class="click-button__mark" viewBox="0 0 56 56" aria-hidden="true"><circle cx="28" cy="28" r="25" fill="var(--mark-red)" stroke="var(--mark-ring)" stroke-width="3"/></svg>
        Hosting
      </a>
    </li>
    <li>
      <a class="click-button click-button--consulting" href="#">
        <svg class="click-button__mark" viewBox="0 0 56 56" aria-hidden="true"><circle cx="28" cy="28" r="25" fill="var(--mark-red)" stroke="var(--mark-ring)" stroke-width="3"/></svg>
        Konsulentydelser
      </a>
    </li>
    <li>
      <a class="click-button click-button--competences" href="#">
        <svg class="click-button__mark" viewBox="0 0 56 56" aria-hidden="true"><circle cx="28" cy="28" r="25" fill="var(--mark-red)" stroke="var(--mark-ring)" stroke-width="3"/></svg>
        Kompetencer
      </a>
    </li>
  </ul>
</body>
</html>
```